Forge Youth Now Website Re-design

The goal of this website redesign is to give Forge Youth Now, a nonprofit focused on recruiting conservative candidates for public office to state and local positions, a platform that balances youthful energy with a sense of maturity and credibility. This site should not only inspire young conservatives across the country to get involved but also position the organization as a leader in cultivating the next generation of public servants. A clean, professional layout will convey trustworthiness, while bold visuals, clean animations, and design motifs will reinforce the patriotic and dynamic nature of the brand. Central to this design is an interactive or static map showcasing our Bright Torches from across the nation as the main home page, helping users quickly understand the breadth of the movement. See design brief for more.

Target Market(s)

18-35 year old American political conservatives

Coding

Coded - Design and coding required

Number of Pages Required

5+ page

Font styles to use
Sans Serif

Requirements
Nice to have
• An active or Static map that is representative of our membership. We will provide data but an example will do

```html
<!DOCTYPE html>
<html lang="en">
<head>
<meta charset="utf-8">
<title>About – Forge Youth Now</title>
<link rel="stylesheet" href="https://fonts.googleapis.com/css2?family=League+Spartan:wght@600;700&family=Figtree:wght@400;500;600;700&display=swap">
<style>
:root{
  --red:#b2233a;
  --plum:#6b3a72;
  --blue:#1b53a8;
  --ink:#24232b;
  --white:#ffffff;
  --portrait:#c9c3c8;
  --line:#c58ea0;
}
*{margin:0;padding:0;box-sizing:border-box}
html,body{width:1200px;height:2492px;overflow:hidden}
body{position:relative;background:var(--white);font-family:"Figtree",sans-serif;color:var(--ink)}
.abs{position:absolute}
.heading{font-family:"League Spartan",sans-serif;font-weight:700}

/* backgrounds */
.band{position:absolute;left:0;width:1200px}

/* nav */
.site-nav{position:absolute;left:0;top:0;width:1200px;height:87px;background:rgba(255,255,255,.1)}
.brand{position:absolute;left:40px;top:30px;font-family:"Figtree",sans-serif;font-weight:700;font-size:15px;color:var(--white);display:flex;align-items:center;gap:7px}
.brand .dot{width:10px;height:10px;border-radius:50%;background:var(--white)}
.nav-links{position:absolute;top:36px;left:408px;display:flex;gap:37px;font-size:11px;color:var(--white);list-style:none}
.nav-links .active{font-weight:700}
.btn-donate{position:absolute;left:1088px;top:31px;width:74px;height:25px;background:var(--white);border-radius:3px;color:var(--blue);font-size:10px;font-weight:700;display:flex;align-items:center;justify-content:center}

/* hero */
.hero-title{position:absolute;top:143px;width:1200px;text-align:center;color:var(--white);font-size:36px;line-height:51px}
.hero-text{position:absolute;top:267px;left:350px;width:500px;text-align:center;color:var(--white);font-size:11px;line-height:17.5px}

/* mission */
.mission-title{left:215px;top:506px;font-size:28px;color:var(--ink)}
.mission-text{left:216px;top:553px;width:270px;font-size:10.5px;line-height:16.3px}
.btn-outline{left:216px;top:655px;width:87px;height:24px;border:1px solid var(--red);border-radius:3px;color:var(--blue);font-size:10px;font-weight:700;display:flex;align-items:center;justify-content:center}
.mission-back{left:551px;top:477px;width:394px;height:280px;background:linear-gradient(90deg,var(--red),#a2304a 60%,#6c3d78)}
.mission-photo{left:591px;top:433px;width:393px;height:281px;background:linear-gradient(160deg,#6f9ad6 0%,#a9c6ea 55%,#c9b2b0 100%)}

/* founder */
.portrait-ring{left:465px;top:815px;width:270px;height:270px;border-radius:50%;background:var(--white)}
.portrait-grad{left:475px;top:825px;width:250px;height:250px;border-radius:50%;background:linear-gradient(200deg,var(--red),#8a3a63 40%,#3a4f9c)}
.portrait-photo{left:485px;top:835px;width:230px;height:230px;border-radius:50%;background:radial-gradient(circle at 50% 45%,#6a5a52,#2a2726 70%)}
.founder-name{left:320px;top:1113px;color:var(--white);font-size:27px;white-space:nowrap}
.founder-name small{font-size:21px;font-weight:600}
.founder-copy{left:321px;top:1175px;width:560px;color:var(--white);font-size:10.5px;line-height:16.3px}
.founder-copy p+p{margin-top:16px}
.signature{left:700px;top:1388px;width:170px;height:72px;background:linear-gradient(90deg,rgba(30,20,40,.0),rgba(30,20,40,.18),rgba(30,20,40,.0))}

/* leaders */
.leaders-title{left:215px;top:1557px;font-size:28px;line-height:31px}
.leaders-text{left:216px;top:1635px;width:240px;font-size:10.5px;line-height:16.3px}
.card{position:absolute;width:244px;text-align:center;color:var(--white)}
.card svg{position:absolute;left:0;top:0}
.card .ring{position:absolute;left:57px;width:130px;height:130px;border-radius:50%;background:var(--white)}
.card .ring-grad{position:absolute;left:62px;width:120px;height:120px;border-radius:50%;background:linear-gradient(20deg,#3a4f9c,#7a3c6c 55%,var(--red))}
.card .photo{position:absolute;left:69px;width:106px;height:106px;border-radius:50%;background:var(--portrait)}
.card .name{position:absolute;left:0;width:244px;font-size:17.5px}
.card .role{position:absolute;left:0;width:244px;font-size:9.5px;font-weight:700;line-height:15px}
.card .bio{position:absolute;left:25px;width:194px;font-size:9.5px;line-height:19px}
.card.light{background:var(--white);border-radius:6px;box-shadow:0 2px 10px rgba(40,30,60,.12);color:var(--ink)}
.card.light .halo{position:absolute;left:50px;top:21px;width:144px;height:144px;border-radius:50%;background:rgba(255,255,255,.35)}

/* footer */
.footer-brand{top:2286px;width:1200px;text-align:center;color:var(--white);font-size:28px;font-weight:700}
.socials{top:2364px;left:557px;display:flex;gap:8px}
.socials span{width:16px;height:16px;border-radius:50%;background:var(--white)}
.footer-links{top:2397px;width:1200px;text-align:center;color:var(--white);font-size:8.5px;list-style:none}
.footer-links li{display:inline}
.footer-links li+li::before{content:"|";margin:0 7px}
.footer-rule{left:216px;top:2433px;width:768px;height:1px;background:rgba(255,255,255,.35)}
.copyright{top:2457px;width:1200px;text-align:center;color:var(--white);font-size:8.5px}
</style>
</head>
<body>

<svg class="band" style="top:0" width="1200" height="2492" viewBox="0 0 1200 2492" aria-hidden="true">
  <defs>
    <linearGradient id="brandGrad" x1="0" y1="0.6" x2="1" y2="0.4">
      <stop offset="0" stop-color="#b2233a"/>
      <stop offset="0.45" stop-color="#8f2d55"/>
      <stop offset="0.65" stop-color="#5d3d7a"/>
      <stop offset="1" stop-color="#1b53a8"/>
    </linearGradient>
    <linearGradient id="founderGrad" x1="0" y1="0.7" x2="1" y2="0.3">
      <stop offset="0" stop-color="#b2233a"/>
      <stop offset="0.45" stop-color="#a22a44"/>
      <stop offset="0.7" stop-color="#6a3b74"/>
      <stop offset="1" stop-color="#1b53a8"/>
    </linearGradient>
  </defs>
  <path d="M0 0H1200V307Q600 409 0 307Z" fill="url(#brandGrad)"/>
  <path d="M0 872Q600 1014 1200 872V1500H0Z" fill="url(#founderGrad)"/>
  <rect x="0" y="2219" width="1200" height="273" fill="url(#brandGrad)"/>
</svg>

<header class="site-nav">
  <div class="brand"><span class="dot"></span>Forge Youth Now</div>
  <ul class="nav-links">
    <li>Home</li><li class="active">About</li><li>Contact</li><li>Bright Torches</li><li>Become a Leader</li>
  </ul>
  <div class="btn-donate">Donate</div>
</header>

<section>
  <h1 class="hero-title heading">Our Mission, Vision<br>&amp; Our Leadership Team</h1>
  <p class="hero-text">Our vision is to empower Generation Z leaders to shape the future by advancing the founding values of limited government, free markets, personal responsibility, and fiscal restraint.</p>
</section>

<section>
  <h2 class="abs heading mission-title">ITS TIME</h2>
  <p class="abs mission-text">Our mission is to empower and mentor conservative trailblazers from Generation Z to pursue leadership opportunities, including public office that allow them to work toward a more constitutionally-focused government.</p>
  <div class="abs btn-outline">Learn More</div>
  <div class="abs mission-back"></div>
  <div class="abs mission-photo" role="img" aria-label="Photo of a young woman holding an American flag against a blue sky"></div>
</section>

<section>
  <div class="abs portrait-ring"></div>
  <div class="abs portrait-grad"></div>
  <div class="abs portrait-photo" role="img" aria-label="Portrait photo of the founder and president"></div>
  <h2 class="abs heading founder-name">EVAN MERCER, <small>FOUNDER &amp; PRESIDENT</small></h2>
  <div class="abs founder-copy">
    <p>Forge Youth Now will recruit and find leaders within college campuses, grassroots organizations, and civilian groups who are able, willing, and ready to run for state and local office and fulfill other public service opportunities. This is executed by giving this next generation the confidence and assistance needed, leading to thousands of young leaders working to spread conservative values across the county.</p>
    <p>This organization will mobilize thousands of free thinking young people to run for office, win, and make substantial changes to our country.</p>
    <p>This is a nationwide movement with a diverse leadership team. There is a vast network of policy makers at the state and local level that each have a unique ability to guide and connect aspiring lawmakers. With their guidance, we will be able to raise up Generation Z candidates and leaders that value conservative policies.</p>
  </div>
  <div class="abs signature" role="img" aria-label="Handwritten signature of the founder"></div>
</section>

<section>
  <h2 class="abs heading leaders-title">MEET OUR<br>LEADERS</h2>
  <p class="abs leaders-text">Forge Youth Now is spearheaded by young leaders who are ready to help.</p>

  <svg width="0" height="0" aria-hidden="true" style="position:absolute">
    <defs>
      <linearGradient id="cardGrad" x1="0" y1="0.75" x2="1" y2="0.25">
        <stop offset="0" stop-color="#b2233a"/>
        <stop offset="0.55" stop-color="#7a3866"/>
        <stop offset="1" stop-color="#2350a4"/>
      </linearGradient>
    </defs>
  </svg>

  <article class="card" style="left:479px;top:1563px;height:278px">
    <svg width="244" height="278"><path d="M0 60Q122 20 244 60V278H0Z" fill="url(#cardGrad)"/></svg>
    <div class="ring" style="top:-3px"></div><div class="ring-grad" style="top:2px"></div>
    <div class="photo" style="top:9px" role="img" aria-label="Leader portrait"></div>
    <h3 class="name heading" style="top:153px">EVAN MERCER</h3>
    <p class="role" style="top:175px">Forge Youth Now<br>Founder &amp; President</p>
    <p class="bio" style="top:215px">Lorem Ipsum is simply dummy text of the printing and typesetting industry.</p>
  </article>

  <article class="card light" style="left:741px;top:1563px;height:299px">
    <svg width="244" height="110"><path d="M0 0H244V96Q122 52 0 96Z" fill="url(#cardGrad)"/></svg>
    <div class="halo"></div>
    <div class="ring" style="top:28px"></div><div class="ring-grad" style="top:33px"></div>
    <div class="photo" style="top:40px" role="img" aria-label="Leader portrait"></div>
    <h3 class="name heading" style="top:180px">CARLA BENTON</h3>
    <p class="role" style="top:202px">Co-Founder<br>State Representative (FL – 36)</p>
    <p class="bio" style="top:237px">Lorem Ipsum is simply dummy text of the printing and typesetting industry.</p>
  </article>

  <article class="card" style="left:216px;top:1878px;height:278px">
    <svg width="244" height="278"><path d="M0 60Q122 20 244 60V278H0Z" fill="url(#cardGrad)"/></svg>
    <div class="ring" style="top:-3px"></div><div class="ring-grad" style="top:2px"></div>
    <div class="photo" style="top:9px" role="img" aria-label="Leader portrait"></div>
    <h3 class="name heading" style="top:153px">TESSA ROWAN</h3>
    <p class="role" style="top:175px">Co-Founder<br>State Representative (FL – 51)</p>
    <p class="bio" style="top:215px">Lorem Ipsum is simply dummy text of the printing and typesetting industry.</p>
  </article>

  <article class="card" style="left:479px;top:1878px;height:278px">
    <svg width="244" height="278"><path d="M0 60Q122 20 244 60V278H0Z" fill="url(#cardGrad)"/></svg>
    <div class="ring" style="top:-3px"></div><div class="ring-grad" style="top:2px"></div>
    <div class="photo" style="top:9px" role="img" aria-label="Leader portrait"></div>
    <h3 class="name heading" style="top:153px">JULIAN HALE</h3>
    <p class="role" style="top:175px">Co-Founder<br>State Rep (NH – Hillsborough 29)</p>
    <p class="bio" style="top:215px">Lorem Ipsum is simply dummy text of the printing and typesetting industry.</p>
  </article>

  <article class="card" style="left:741px;top:1878px;height:278px">
    <svg width="244" height="278"><path d="M0 60Q122 20 244 60V278H0Z" fill="url(#cardGrad)"/></svg>
    <div class="ring" style="top:-3px"></div><div class="ring-grad" style="top:2px"></div>
    <div class="photo" style="top:9px" role="img" aria-label="Leader portrait"></div>
    <h3 class="name heading" style="top:153px">MILES HARPER</h3>
    <p class="role" style="top:175px">Co-Founder<br>Executive Director</p>
    <p class="bio" style="top:215px">Lorem Ipsum is simply dummy text of the printing and typesetting industry.</p>
  </article>
</section>

<footer>
  <div class="abs footer-brand">Forge Youth Now</div>
  <div class="abs socials" aria-label="Social links"><span></span><span></span><span></span><span></span></div>
  <ul class="abs footer-links">
    <li>Terms of Use</li><li>Privacy Policy</li><li>Security Policy</li><li>Cookie Settings</li>
  </ul>
  <div class="abs footer-rule"></div>
  <p class="abs copyright">© Copyright 2025 Forge Youth Now. All rights reserved. Northlane Studio.</p>
</footer>

</body>
</html>
```